Recycling Exhibition Web Design Project

We are developing a new website for a exhibition we have just taken over. The previous site is very basic and we require a complete redesign. The site should be designed to engage with and attract those who work in or provide services to the multibillion dollar wastes and recycling industry in the Asia pacific region. These will include Federal & State Governments, City councils, private sector, industry associations and other key bodies, education facilities.

KTLO is the premier waste and recycling event in the Asia Pacific region and known as place where the industry meets to share innovations, gain knowledge, to network and do business.
• Innovation
• Knowledge transfer
• Industry Networking
• Trade
Key point: need to reflect that 2012 show will attract large numbers of quality visitors from across wide range of the industry – city councils, facilities managers, etc

Site should deliver 3 key objectives.
1. Stimulate interest those who work in or provide services to the wastes and recycling industry by providing simple to access, relevant and topical information about the Expo, the Seminars, the Key Features, the sub activities and the key benefits to them.
2. Provide a platform that supports / improves EP by providing a range of interactive components – ie floor plan / video. In addition options for sales enquiries, registration, general feedback
3. Provide a way to highlight / showcase sponsors, show features and other key assets. (possibly a carousel above the fold)

We really like the dunmar website so a take on this could be good (http://www.dunmar-example.com.au/). Also we want to try to reinforce the brand so we should use the event as the hero image/banner.

Previous website - http://www.ktlo-example.com.au/

Target Market(s)

The site should be designed to engage with and attract those who work in or provide services to the multibillion dollar wastes and recycling industry

Industry/Entity Type

Recycling

Requirements
Must have
• The icons on the current site work quite well so inclusion as CTAs would be preferable.

Other key areas are

• Seminar Delegate & Visitor Registration
• Exhibitor Prospectus
• Floorplan
• Conference / Seminar content
• Social media + blog

Site visitors will need to feel like they are part of a community.
Site should reflect/display key industry stats & stats from 2011 expo

Please see the attached brief for more details and site map for menu items.

```html
<!DOCTYPE html>
<html lang="en">
<head>
<meta charset="utf-8">
<title>KTLO – Southern Waste &amp; Resource Expo</title>
<link rel="stylesheet" href="https://fonts.googleapis.com/css2?family=Yanone+Kaffeesatz:wght@400;500;600&family=Open+Sans:wght@400;600&family=Arimo:wght@400&display=swap">
<style>
:root{
  --bark:#8b867a;
  --bark-dark:#6f6a5f;
  --frame:#4d4a45;
  --paper:#f6f4ee;
  --panel:#f2f1ec;
  --panel-line:#d9d3c0;
  --green:#6e8f55;
  --green-dark:#557240;
  --green-text:#7d9c60;
  --red:#c9524a;
  --red-dark:#9e3a34;
  --gold:#c8b27a;
  --tan:#c9b98c;
  --tan-text:#7b6d4c;
  --ink:#3d3a36;
  --grey-text:#7c7466;
  --footer:#b7ae96;
  --white:#ffffff;
}
*{box-sizing:border-box;margin:0;padding:0}
html,body{width:1200px;height:900px;overflow:hidden}
body{
  position:relative;
  background:linear-gradient(160deg,#938e82 0%,var(--bark) 45%,var(--bark-dark) 100%);
  font-family:Arimo,Arial,sans-serif;color:var(--ink);
}
.util-links{
  position:absolute;left:947px;top:0;width:184px;height:22px;
  background:#d9d1bb;border-radius:0 0 4px 4px;
  display:flex;justify-content:center;align-items:center;gap:8px;
  font:12px Arimo,Arial,sans-serif;color:var(--ink);
}
.util-links .sep{color:#9a9080}
.brand{position:absolute;left:190px;top:30px;display:flex;align-items:baseline;gap:12px}
.brand-name{font:500 62px/1 'Yanone Kaffeesatz',sans-serif;color:var(--ink);letter-spacing:.5px}
.frame{
  position:absolute;left:91px;top:117px;width:1022px;height:700px;
  background:var(--frame);border-radius:3px;box-shadow:0 4px 14px rgba(0,0,0,.45);
}
.sheet{position:absolute;left:12px;top:12px;width:998px;height:676px;background:var(--paper)}
.main-nav{position:absolute;left:59px;top:137px;width:1089px;height:56px}
.main-nav svg{position:absolute;left:0;top:0}
.main-nav ul{position:absolute;inset:0;list-style:none}
.main-nav li{
  position:absolute;top:18px;transform:translateX(-50%);white-space:nowrap;
  font:600 16px 'Open Sans',sans-serif;color:var(--white);text-shadow:0 1px 1px rgba(0,0,0,.4);
}
.hero{
  position:absolute;left:108px;top:193px;width:985px;height:121px;overflow:hidden;
  background:linear-gradient(180deg,#d9ddd6 0%,#b9c0b2 45%,#8c8f73 100%);
}
.hero-photo{position:absolute;inset:0;background:linear-gradient(90deg,rgba(70,60,45,.35) 0%,rgba(220,225,220,.2) 45%,rgba(90,80,60,.2) 100%)}
.hero-title{
  position:absolute;left:50px;top:35px;
  font:500 32px/1 'Yanone Kaffeesatz',sans-serif;color:var(--white);text-shadow:0 1px 3px rgba(0,0,0,.5);
}
.sub-nav{position:absolute;left:0;bottom:0;width:100%;height:28px;background:rgba(45,42,36,.7)}
.sub-nav span{
  position:absolute;top:7px;transform:translateX(-50%);white-space:nowrap;
  font:12.5px 'Open Sans',sans-serif;color:#f0ede4;
}
.card{position:absolute;background:var(--panel);border:1px solid var(--panel-line);box-shadow:0 1px 2px rgba(0,0,0,.08)}
.conference{left:125px;top:332px;width:634px;height:137px}
.tag{position:absolute;display:flex;align-items:center;justify-content:center;font:500 30px/1 'Yanone Kaffeesatz',sans-serif;color:var(--white)}
.tag-year{left:117px;top:354px;width:94px;height:50px;background:var(--red);box-shadow:0 2px 3px rgba(0,0,0,.25);clip-path:polygon(0 0,100% 0,92% 50%,100% 100%,0 100%)}
.section-title{position:absolute;font:500 22px/1 'Yanone Kaffeesatz',sans-serif;letter-spacing:.5px}
.conference-title{left:223px;top:348px;color:var(--red)}
.conference-text{position:absolute;left:223px;top:372px;width:520px;font:14.3px/21px Arimo,Arial,sans-serif;color:var(--ink)}
.city-photo{
  position:absolute;left:771px;top:333px;width:309px;height:133px;border:2px solid var(--white);
  background:linear-gradient(180deg,#6fa6d6 0%,#9cc3e2 40%,#c9c4b4 55%,#2f6f9a 70%,#1e5579 100%);
}
.program{left:125px;top:483px;width:957px;height:255px}
.tag-program{left:117px;top:495px;width:97px;height:32px;background:var(--green);font-size:19px;clip-path:polygon(0 0,100% 0,93% 50%,100% 100%,0 100%)}
.program-title{left:224px;top:501px;color:var(--green-text)}
.session{position:absolute;left:120px;display:flex;align-items:center;height:30px;white-space:nowrap}
.session-date{
  width:65px;height:30px;background:var(--gold);color:var(--white);
  font:500 20px/30px 'Yanone Kaffeesatz',sans-serif;text-align:center;
  clip-path:polygon(0 0,100% 0,94% 50%,100% 100%,0 100%);
}
.session-name{margin-left:14px;font:500 23px/1 'Yanone Kaffeesatz',sans-serif;color:#4d4943}
.session-info{margin-left:18px;font:14.5px Arimo,Arial,sans-serif;color:var(--grey-text)}
.register-ribbon{position:absolute;left:994px;top:648px}
.categories{
  position:absolute;left:100px;top:754px;width:1004px;height:49px;background:var(--tan);
  display:flex;justify-content:space-around;align-items:center;padding:0 6px;
}
.category{display:flex;align-items:center;gap:6px;font:11.5px/1.05 Arimo,Arial,sans-serif;color:var(--tan-text);text-align:center}
.category svg{flex:none}
.site-footer{position:absolute;left:0;top:846px;width:1200px;height:54px;background:var(--footer);border-top:1px solid #cfc7b0}
.social{position:absolute;top:10px;left:88px;display:flex;gap:15px}
.social span{width:35px;height:35px;border-radius:50%;background:#4a4741;border:2px solid #d6cfbb;display:flex;align-items:center;justify-content:center}
.footer-info{position:absolute;left:420px;top:19px;font:13px Arimo,Arial,sans-serif;color:#4d4943}
.footer-info .sep{color:#8a826f;margin:0 7px}
.copyright{position:absolute;right:83px;top:19px;font:13px Arimo,Arial,sans-serif;color:#4d4943}
</style>
</head>
<body>
<nav class="util-links"><span>Register</span><span class="sep">|</span><span>Exhibitor Login</span></nav>

<header class="brand"><span class="brand-name">Southern Waste &amp; Resource Expo</span></header>

<div class="frame"><div class="sheet"></div></div>

<nav class="main-nav">
  <svg width="1089" height="56" viewBox="0 0 1089 56">
    <polygon points="0,14 30,14 30,56 12,56 0,50 10,35" fill="var(--green-dark)"/>
    <polygon points="1089,14 1059,14 1059,56 1077,56 1089,50 1079,35" fill="var(--green-dark)"/>
    <rect x="10" y="0" width="1069" height="50" fill="var(--green)"/>
    <rect x="10" y="4" width="1069" height="42" fill="none" stroke="rgba(255,255,255,.35)" stroke-dasharray="3 3"/>
  </svg>
  <ul>
    <li style="left:117px">HOME</li>
    <li style="left:207px">ABOUT</li>
    <li style="left:339px">WHAT'S ON</li>
    <li style="left:485px">REGISTER</li>
    <li style="left:648px">HOW TO EXHIBIT</li>
    <li style="left:806px">BLOG</li>
    <li style="left:950px">CONTACT US</li>
  </ul>
</nav>

<section class="hero">
  <div class="hero-photo" role="img" aria-label="Misty forest with four coloured recycling bins in a row"></div>
  <h1 class="hero-title">Join KTLO on 21 &amp; 22 November 2012</h1>
  <nav class="sub-nav">
    <span style="left:111px">EXHIBITION PROSPECTUS</span>
    <span style="left:271px">FLOOR PLAN</span>
    <span style="left:435px">CONFERENCES / SEMINARS</span>
    <span style="left:602px">REGISTRATION</span>
    <span style="left:747px">FREE WORKSHOPS</span>
    <span style="left:896px">OUR SPONSORS</span>
  </nav>
</section>

<section class="card conference"></section>
<div class="tag tag-year">2012</div>
<h2 class="section-title conference-title">CONFERENCE PROGRAM</h2>
<p class="conference-text">Prestigious industry experts discuss new legislation, technologies and innovations in resource recovery. This unique combination of quality content and subsidised registration fees will ensure all industry participants have access to the highest standard of information concerning critical issues facing our industry.</p>
<div class="city-photo" role="img" aria-label="Harbour city skyline with opera house and boats on the water"></div>

<section class="card program"></section>
<div class="tag tag-program">PROGRAM</div>
<h2 class="section-title program-title">VIEW FULL PROGRAM</h2>
<div class="session" style="top:546px"><span class="session-date">21 Nov</span><span class="session-name">Carbon Price &amp; Carbon Farming Initiative</span><span class="session-info">Morning &nbsp;/ &nbsp;$185 (GST incl.) &nbsp;/ &nbsp;Includes lunch</span></div>
<div class="session" style="top:593px"><span class="session-date">21 Nov</span><span class="session-name">Product Stewardship &amp; Innovation</span><span class="session-info">Afternoon (leads into free Welcome Reception 4-6pm) &nbsp;/ &nbsp;$99 (GST incl.) &nbsp;/ &nbsp;Includes lunch</span></div>
<div class="session" style="top:639px"><span class="session-date">22 Nov</span><span class="session-name">Waste to Energy &amp; Local Government AWT Procurement</span><span class="session-info">Morning &nbsp;/ &nbsp;$99 (GST incl.) &nbsp;/ &nbsp;Includes lunch</span></div>
<div class="session" style="top:686px"><span class="session-date">21 Nov</span><span class="session-name">Green Buildings: Design, Construction &amp; Operation</span><span class="session-info">Afternoon / &nbsp;$99 (GST incl.) &nbsp;/ &nbsp;Includes lunch</span></div>

<svg class="register-ribbon" width="96" height="96" viewBox="0 0 96 96">
  <polygon points="94,0 94,30 30,94 0,94" fill="var(--red)"/>
  <polygon points="94,0 96,4 96,34 94,30" fill="var(--red-dark)"/>
  <text x="58" y="59" transform="rotate(-45 58 59)" text-anchor="middle" font-family="'Yanone Kaffeesatz',sans-serif" font-size="15" fill="#fff">★ REGISTER ★</text>
</svg>

<nav class="categories">
  <div class="category"><svg width="30" height="28" viewBox="0 0 30 28"><polygon points="15,2 28,26 2,26" fill="none" stroke="var(--tan-text)" stroke-width="2.5"/><rect x="14" y="10" width="2.5" height="9" fill="var(--tan-text)"/></svg>Hazardous<br>Waste</div>
  <div class="category"><svg width="28" height="28" viewBox="0 0 28 28"><rect x="6" y="6" width="16" height="18" rx="2" fill="none" stroke="var(--tan-text)" stroke-width="2.5" transform="rotate(-20 14 14)"/></svg>Disposal</div>
  <div class="category"><svg width="28" height="28" viewBox="0 0 28 28"><path d="M4 16 Q14 4 24 16 Z" fill="var(--tan-text)"/><rect x="6" y="18" width="16" height="6" fill="var(--tan-text)"/></svg>Compost</div>
  <div class="category"><svg width="24" height="28" viewBox="0 0 24 28"><circle cx="12" cy="11" r="8" fill="none" stroke="var(--tan-text)" stroke-width="2.5"/><rect x="8" y="20" width="8" height="5" fill="var(--tan-text)"/></svg>Energy<br>from Waste</div>
  <div class="category"><svg width="22" height="28" viewBox="0 0 22 28"><rect x="3" y="6" width="16" height="20" fill="var(--tan-text)"/><rect x="1" y="2" width="20" height="3" fill="var(--tan-text)"/></svg>Bin Liners<br>&amp; Containers</div>
  <div class="category"><svg width="30" height="28" viewBox="0 0 30 28"><circle cx="10" cy="16" r="7" fill="none" stroke="var(--tan-text)" stroke-width="3"/><circle cx="22" cy="9" r="5" fill="none" stroke="var(--tan-text)" stroke-width="3"/></svg>Machinery<br>&amp; Equipment</div>
  <div class="category"><svg width="28" height="28" viewBox="0 0 28 28"><path d="M2 6 L13 8 L13 26 L2 24 Z M15 8 L26 6 L26 24 L15 26 Z" fill="var(--tan-text)"/></svg>Service &amp;<br>Solutions</div>
  <div class="category"><svg width="34" height="28" viewBox="0 0 34 28"><rect x="2" y="7" width="20" height="13" fill="var(--tan-text)"/><path d="M22 11 H28 L32 16 V20 H22 Z" fill="var(--tan-text)"/><circle cx="9" cy="22" r="3.5" fill="var(--tan-text)"/><circle cx="26" cy="22" r="3.5" fill="var(--tan-text)"/></svg>Vehicles<br>&amp; Plants</div>
  <div class="category"><svg width="28" height="28" viewBox="0 0 28 28"><circle cx="14" cy="14" r="10" fill="none" stroke="var(--tan-text)" stroke-width="3"/><polygon points="22,2 26,12 17,10" fill="var(--tan-text)"/></svg>Recycled<br>Products</div>
</nav>

<footer class="site-footer">
  <div class="social">
    <span aria-label="Social link one"></span>
    <span aria-label="Social link two"></span>
    <span aria-label="Social link three"></span>
    <span aria-label="Blog"></span>
    <span aria-label="Email"><svg width="18" height="13" viewBox="0 0 18 13"><rect x="1" y="1" width="16" height="11" fill="none" stroke="#e8e2d2" stroke-width="1.6"/><polyline points="1,1 9,8 17,1" fill="none" stroke="#e8e2d2" stroke-width="1.6"/></svg></span>
  </div>
  <p class="footer-info">21 &amp; 22 November 2012<span class="sep">|</span>All Enquiries: +61 (3) 9000 4517</p>
  <p class="copyright">© 2012 Southern Waste &amp; Resource Expo</p>
</footer>
</body>
</html>
```